Newsletter Design Project

I need a new design for a monthly newsletter that I do for Marbury Lane Open College Ipswich. I have been doing the same thing since 2009. We are based in Brisbane and we run classes for semi retired and retired people. I write about social activities, class activities, vacancies etc. I take photos and include them we hhave a logo that I always use. and would just like the newsletter to look different and fresh. The logo is Blue

```html
<!DOCTYPE html>
<html lang="en">
<head>
<meta charset="utf-8">
<title>Marbury Lane Open College Ipswich – Monthly Newsletter</title>
<link href="https://fonts.googleapis.com/css2?family=Arimo:wght@400;700&display=swap" rel="stylesheet">
<style>
  :root {
    --brand-blue: #2a7dc9;
    --brand-blue-deep: #1e69b1;
    --divider-blue: #4f95d6;
    --button-navy: #163f6e;
    --ink: #333333;
    --paper: #ffffff;
  }
  * { margin: 0; padding: 0; box-sizing: border-box; }
  html, body { width: 1200px; height: 3000px; overflow: hidden; background: var(--paper); }
  body { font-family: "Arimo", Arial, sans-serif; color: var(--ink); position: relative; }

  .topbar {
    position: absolute; left: 0; top: 0; width: 1200px; height: 160px;
    background: var(--brand-blue); border-top: 8px solid var(--brand-blue-deep);
    color: var(--paper);
  }
  .topbar__tagline { position: absolute; left: 40px; top: 64px; font-size: 23px; }
  .topbar__meta { position: absolute; right: 40px; top: 62px; font-weight: 700; font-size: 26px; }
  .topbar__issue { font-size: 21px; margin-left: 12px; }

  .masthead { position: absolute; left: 0; top: 160px; width: 1200px; height: 206px; }
  .masthead__name { position: absolute; left: 44px; top: 76px; font-size: 40px; color: var(--brand-blue); }
  .masthead__call { position: absolute; right: 52px; top: 98px; font-size: 39px; font-weight: 700; color: var(--ink); }
  .masthead__number { color: var(--brand-blue); }

  .photo { position: absolute; }
  .photo--hero {
    left: 0; top: 366px; width: 1200px; height: 652px;
    background: linear-gradient(90deg, #e9ecee 0%, #c9c6c2 45%, #6f6a66 80%, #dcdad6 100%);
  }
  .photo--row { left: 0; width: 588px; height: 344px; }
  .photo--painting { background: linear-gradient(90deg, #e8e3da 0%, #c7b9a6 60%, #b3a898 100%); }
  .photo--computer { background: linear-gradient(90deg, #d9dde2 0%, #b9bec6 60%, #e6e8ea 100%); }
  .photo--tutor { background: linear-gradient(90deg, #cfd3d8 0%, #d9c7b5 55%, #eceef0 100%); }

  .feature {
    position: absolute; left: 0; top: 1018px; width: 1200px; height: 362px;
    background: var(--brand-blue); color: var(--paper);
  }
  .feature__title { position: absolute; left: 40px; top: 62px; font-size: 46px; font-weight: 400; }
  .feature__text { position: absolute; left: 48px; top: 144px; width: 1120px; font-size: 23px; line-height: 44px; }

  .read-more {
    position: absolute; left: 0; bottom: 0; width: 100%; height: 82px;
    border-top: 2px solid var(--divider-blue);
    display: flex; align-items: center; gap: 26px; padding-left: 40px;
    font-size: 24px; font-weight: 700; color: var(--paper);
  }
  .read-more__icon {
    width: 38px; height: 26px; background: var(--button-navy);
    display: flex; align-items: center; justify-content: center;
  }
  .story .read-more { height: 98px; }

  .story {
    position: absolute; left: 612px; width: 588px; height: 350px;
    background: var(--brand-blue); color: var(--paper);
  }
  .story__title { position: absolute; left: 40px; top: 66px; font-size: 36px; font-weight: 400; }
  .story__text { position: absolute; left: 48px; top: 124px; width: 470px; font-size: 23px; line-height: 44px; }

  .rule { position: absolute; left: 0; top: 2630px; width: 1200px; height: 6px; background: var(--brand-blue); }

  .footer-note {
    position: absolute; left: 0; top: 2692px; width: 1200px; text-align: center;
    font-size: 23px; line-height: 40px; color: var(--ink);
  }
  .footer-note__copy { color: var(--brand-blue); }

  .social-bar {
    position: absolute; left: 0; top: 2882px; width: 1200px; height: 118px;
    background: var(--brand-blue);
    display: flex; justify-content: center; align-items: center; gap: 14px;
  }
  .social-bar__dot { width: 54px; height: 54px; border-radius: 50%; background: var(--paper); }
</style>
</head>
<body>

  <header class="topbar">
    <p class="topbar__tagline">Learning, friendship and fun after work</p>
    <p class="topbar__meta">August 07,2013<span class="topbar__issue">Issue # 258</span></p>
  </header>

  <section class="masthead">
    <p class="masthead__name">Marbury Lane Open College Ipswich</p>
    <p class="masthead__call">Call Us : <span class="masthead__number">1800-555-0142</span></p>
  </section>

  <div class="photo photo--hero" role="img" aria-label="Members of the college smiling together at the start of the new term"></div>

  <section class="feature">
    <h1 class="feature__title">Spring term classes are now open for enrolment</h1>
    <p class="feature__text">This term brings watercolour painting, beginners' Italian, local history walks and gentle tai chi in the park. Places fill quickly, so pop into the office or give us a call to reserve your seat.</p>
    <div class="read-more">
      <span class="read-more__icon"><svg width="14" height="14" viewBox="0 0 14 14"><path d="M7 2v10M2 7h10" stroke="#fff" stroke-width="2.4"/></svg></span>
      READ MORE +
    </div>
  </section>

  <div class="photo photo--row photo--painting" style="top:1424px" role="img" aria-label="Members at the Tuesday morning tea and social club"></div>
  <article class="story" style="top:1424px">
    <h2 class="story__title">Morning tea and social club</h2>
    <p class="story__text">Photos from our Tuesday catch-up, plus dates for the next outing.</p>
    <div class="read-more">
      <span class="read-more__icon"><svg width="14" height="14" viewBox="0 0 14 14"><path d="M7 2v10M2 7h10" stroke="#fff" stroke-width="2.4"/></svg></span>
      READ MORE +
    </div>
  </article>

  <div class="photo photo--row photo--computer" style="top:1826px" role="img" aria-label="Students learning tablet and email skills in the computer room"></div>
  <article class="story" style="top:1826px">
    <h2 class="story__title">Computer class vacancies</h2>
    <p class="story__text">Two seats remain in the Thursday tablet and email skills course.</p>
    <div class="read-more">
      <span class="read-more__icon"><svg width="14" height="14" viewBox="0 0 14 14"><path d="M7 2v10M2 7h10" stroke="#fff" stroke-width="2.4"/></svg></span>
      READ MORE +
    </div>
  </article>

  <div class="photo photo--row photo--tutor" style="top:2228px" role="img" aria-label="Our new creative writing tutor in the college lounge"></div>
  <article class="story" style="top:2228px">
    <h2 class="story__title">Welcome our new tutor</h2>
    <p class="story__text">A retired teacher now leads the Friday creative writing circle.</p>
    <div class="read-more">
      <span class="read-more__icon"><svg width="14" height="14" viewBox="0 0 14 14"><path d="M7 2v10M2 7h10" stroke="#fff" stroke-width="2.4"/></svg></span>
      READ MORE +
    </div>
  </article>

  <div class="rule"></div>

  <footer class="footer-note">
    <p>You have received this email because you have subscribed to Postwren as Mail@</p>
    <p>marburylane.example If you no longer wish to receive emails please unsubscribe</p>
    <p class="footer-note__copy">Copyright © 2012 marburylane.example</p>
  </footer>

  <nav class="social-bar" aria-label="Social links">
    <span class="social-bar__dot"></span>
    <span class="social-bar__dot"></span>
    <span class="social-bar__dot"></span>
    <span class="social-bar__dot"></span>
    <span class="social-bar__dot"></span>
    <span class="social-bar__dot"></span>
  </nav>

</body>
</html>
```